Life and business Coaching Business Card and Logo

A new design for new company. We coach people to get the best out of themselves in business, life, health , family, career, relationships.
we work in Professional, executive, business and corporate environment. We use art and the processes of making art to work with getting people to delve into and change their mind maps or the way they are currently thinking so that they can move forward towards their goals strategically.
Updates

Project Deadline Extended
Reason: I have been laid up in bed with back problems and have just been able to get back to view designs. several are quiet good and I have given feedback today. I also want to take my project off refundable status as I will choose a design from this brief. regards Marisol

Target Market(s)

Professional artistic and bold energetic individuals

Industry/Entity Type

Health

Contact Information for Business Card

Vel5Mentoring, Marisol Drayke, Shaping Days Boldly,
Mob:0419586740, Ph: +61 8 95820647,
Professional, Executive, Business and Corporate Coach

Requirements
Must have
• a logo that can be used on all promotional and stationary material.
Should contain a person and be bold/colourful, simple and artistic.
Nice to have
• Room to place qualifications of Business

```html
<!DOCTYPE html>
<html lang="en">
<head>
<meta charset="utf-8">
<title>Vel5Mentoring – Business Card</title>
<link rel="stylesheet" href="https://fonts.googleapis.com/css2?family=Questrial&display=swap">
<style>
  :root {
    --violet-light: #bbb5d8;
    --violet-mid: #9a90c2;
    --violet-deep: #6c5f9f;
    --ink-white: #ffffff;
  }
  html, body {
    margin: 0;
    padding: 0;
    width: 1200px;
    height: 675px;
    overflow: hidden;
  }
  .card {
    position: relative;
    width: 1200px;
    height: 675px;
    overflow: hidden;
    background: radial-gradient(ellipse 900px 700px at 444px 374px,
      var(--violet-light) 0%, var(--violet-mid) 45%, var(--violet-deep) 100%);
    font-family: "Questrial", "Century Gothic", sans-serif;
    color: var(--ink-white);
  }
  .brand {
    position: absolute;
    left: 400px;
    top: 150px;
    width: 460px;
    text-align: center;
  }
  .brand-name {
    margin: 0;
    font-size: 66px;
    font-weight: 400;
    line-height: 1;
    letter-spacing: 0.01em;
  }
  .brand-tagline {
    margin: 22px 0 0;
    font-size: 15px;
    letter-spacing: 0.32em;
    text-transform: uppercase;
  }
  .contact {
    position: absolute;
    left: 76px;
    top: 460px;
    margin: 0;
    font-size: 28px;
    line-height: 35px;
    font-style: normal;
  }
  .contact span { display: block; }
</style>
</head>
<body>
  <main class="card">
    <header class="brand">
      <h1 class="brand-name">Vel5Mentoring</h1>
      <p class="brand-tagline">Shaping Days Boldly</p>
    </header>
    <address class="contact">
      <span class="contact-name">Marisol Drayke,</span>
      <span class="contact-role">Professional, Executive</span>
      <span class="contact-role">Business and Corporate Coach</span>
      <span class="contact-phone">Mob:0419586740, Ph: +61 8 95820647</span>
    </address>
  </main>
</body>
</html>
```